Estate Planning Law Firm opening new branch in Florida

I am an experienced estate planning attorney that recently relocated to Florida. Looking for a banner Ad to place on platforms such as YardLoop, Chatterly and Pixmora to create publicity for firm and new leads.

```html
<!DOCTYPE html>
<html lang="en">
<head>
<meta charset="utf-8">
<title>Serenvale Law Firm – Estate &amp; Financial Planning Banner</title>
<link rel="stylesheet" href="https://fonts.googleapis.com/css2?family=Oswald:wght@300;500;600;700&family=Open+Sans:wght@600;700&display=swap">
<style>
  :root {
    --page: #f7f7f7;
    --navy: #252a36;
    --teal: #1a6b6e;
    --ring-light: #d3d6db;
    --ring-mid: #b3b8c0;
    --ring-dark: #2b3a4e;
    --white: #ffffff;
    --arc: rgba(255, 255, 255, 0.42);
  }
  html, body {
    margin: 0;
    padding: 0;
    width: 1200px;
    height: 1200px;
    overflow: hidden;
    background: var(--page);
  }
  .banner {
    display: block;
    width: 1200px;
    height: 1200px;
  }
  .headline {
    font-family: "Oswald", sans-serif;
    font-weight: 700;
    font-size: 94px;
    fill: var(--white);
  }
  .subhead {
    font-family: "Open Sans", sans-serif;
    font-weight: 700;
    font-size: 48px;
    fill: var(--white);
  }
  .person-name {
    font-family: "Oswald", sans-serif;
    font-weight: 700;
    font-size: 62px;
    fill: var(--white);
  }
  .person-role {
    font-family: "Oswald", sans-serif;
    font-weight: 300;
    font-size: 40px;
    fill: var(--white);
  }
  .website {
    font-family: "Oswald", sans-serif;
    font-weight: 700;
    font-size: 52px;
    fill: var(--white);
  }
  .phone {
    font-family: "Oswald", sans-serif;
    font-weight: 600;
    font-size: 84px;
    fill: var(--ring-dark);
  }
  .firm-name {
    font-family: "Oswald", sans-serif;
    font-weight: 500;
    font-size: 44px;
    fill: var(--ring-dark);
  }
  .firm-sub {
    font-family: "Oswald", sans-serif;
    font-weight: 500;
    font-size: 18px;
    fill: var(--ring-dark);
  }
</style>
</head>
<body>
<svg class="banner" viewBox="0 0 1932 1932" xmlns="http://www.w3.org/2000/svg">
  <defs>
    <clipPath id="ad-area">
      <rect x="217" y="214" width="1498" height="1503"/>
    </clipPath>
    <linearGradient id="portrait-tone" x1="0" y1="0" x2="1" y2="1">
      <stop offset="0" stop-color="#c9875a"/>
      <stop offset="0.55" stop-color="#9a6a55"/>
      <stop offset="1" stop-color="#1f2a40"/>
    </linearGradient>
  </defs>

  <g class="ad" clip-path="url(#ad-area)">
    <rect class="ad-base" x="217" y="214" width="1498" height="1503" fill="var(--teal)"/>

    <path class="navy-wave" fill="var(--navy)"
      d="M1610,214 L1715,214 L1715,1717 L217,1717 L217,1255
         C320,1175 420,1160 520,1170 C700,1190 850,1240 960,1280
         C1100,1330 1250,1390 1390,1390 C1490,1390 1520,1290 1510,1220
         C1495,1130 1400,1090 1310,1060 C1150,1000 950,920 850,860
         C720,780 680,620 720,480 C770,330 900,270 1000,270
         C1120,270 1200,320 1280,360 C1340,390 1400,400 1440,390
         C1510,360 1560,290 1610,214 Z"/>

    <path class="contact-band" fill="var(--white)"
      d="M800,1540 L1715,1540 L1715,1717 L605,1717 C700,1690 770,1620 800,1540 Z"/>

    <line class="top-rule" x1="1100" y1="287" x2="1715" y2="287" stroke="var(--white)" stroke-width="3"/>

    <path class="sweep-arc" d="M190,1100 A485,485 0 0 1 945,1225" fill="none" stroke="var(--arc)" stroke-width="40"/>

    <circle class="accent-ring-outer" cx="756" cy="1031" r="105" fill="none" stroke="var(--ring-dark)" stroke-width="8"/>
    <circle class="accent-ring-inner" cx="756" cy="1031" r="45" fill="none" stroke="var(--ring-light)" stroke-width="3" opacity="0.7"/>

    <g class="portrait-frame">
      <circle cx="1297" cy="702" r="340" fill="var(--ring-mid)"/>
      <circle cx="1297" cy="702" r="330" fill="var(--ring-light)"/>
      <circle cx="1297" cy="702" r="315" fill="var(--ring-dark)"/>
      <circle cx="1297" cy="702" r="285" fill="var(--ring-light)"/>
      <circle class="portrait" cx="1297" cy="702" r="256" fill="url(#portrait-tone)"
        role="img" aria-label="Photo of the attorney and the financial planner smiling in front of a brick wall"/>
    </g>

    <g class="firm-badge">
      <circle cx="543" cy="1383" r="241" fill="var(--ring-mid)"/>
      <circle cx="543" cy="1383" r="230" fill="var(--ring-light)"/>
      <circle cx="543" cy="1383" r="210" fill="var(--ring-dark)"/>
      <circle cx="543" cy="1383" r="188" fill="var(--ring-light)"/>
      <circle cx="543" cy="1383" r="165" fill="var(--white)"/>
      <rect class="firm-mark" x="418" y="1362" width="30" height="30" fill="var(--teal)"/>
      <text class="firm-name" x="462" y="1398">SERENVALE</text>
      <text class="firm-sub" x="505" y="1420">LAW FIRM, PLLC</text>
    </g>

    <g class="headline-block">
      <text class="headline" x="285" y="397">ESTATE PLANNING &amp;</text>
      <text class="headline" x="285" y="517" textLength="683" lengthAdjust="spacingAndGlyphs">FINANCIAL PLANNING</text>
      <text class="headline" x="285" y="637">UNDER ONE ROOF</text>
      <line x1="288" y1="702" x2="903" y2="702" stroke="var(--white)" stroke-width="4"/>
      <text class="subhead" x="290" y="797">MELBOURNE, FL ESTATE</text>
      <text class="subhead" x="290" y="862">AND FINANCIAL PLANNING</text>
    </g>

    <g class="team">
      <rect x="943" y="1093" width="14" height="117" fill="var(--ring-light)"/>
      <text class="person-name" x="976" y="1140" textLength="655" lengthAdjust="spacingAndGlyphs">ATTORNEY MARISSA KELLERMAN</text>
      <text class="person-role" x="976" y="1196" letter-spacing="19">ATTORNEY AT LAW</text>
      <rect x="943" y="1255" width="14" height="117" fill="var(--white)"/>
      <text class="person-name" x="982" y="1300" textLength="428" lengthAdjust="spacingAndGlyphs">THOMAS KELLERMAN</text>
      <text class="person-role" x="982" y="1355" letter-spacing="14">FINANCIAL PLANNER</text>
    </g>

    <line class="contact-rule" x1="943" y1="1409" x2="1627" y2="1409" stroke="var(--white)" stroke-width="4"/>
    <text class="website" x="943" y="1490" textLength="625" lengthAdjust="spacingAndGlyphs">www.keepandbuildwealth.com</text>
    <text class="phone" x="940" y="1658" textLength="714" lengthAdjust="spacingAndGlyphs">Phone Call: (321) 555-0147</text>
  </g>
</svg>
</body>
</html>
```